eCommerce Website Design for Electronic Kits

The company is called Kitlorne. We develop electronic kits, parts & tutorials for hobbyists and engineers. I want something bigger than myself. I can develop and code something, but I want it to be more than I can imagine, so I am here. So, if you feel you have something unique but outside my direction, go for it! I am leaning toward a darker, modern, clean look with a "retro feel," maybe purples, bright reds/pinks, or neon. Our competition is https://www.veltorbay.example and https://www.quimzaloft.example

Target Market(s)

Hobyists & Engineers (electronics and 3d printing)

Industry/Entity Type

Electronic parts, kits, PCBs, tutorials

Number of Pages Required

4 page

Font styles to use
Sans Serif

Colors

Designer to choose colors to be used in the design.

Requirements
Must have
• Landing / Main Page, Shopping Cart, Item Detail, Blog Post

```html
<!DOCTYPE html>
<html lang="en">
<head>
<meta charset="utf-8">
<title>Kitlorne — Electronic Kits</title>
<link href="https://fonts.googleapis.com/css2?family=Cabin:wght@500;600;700&family=Roboto:wght@400;500;700&display=swap" rel="stylesheet">
<style>
:root{
  --night:#14071f;
  --plum:#2a0b3a;
  --wine:#5e0f45;
  --magenta:#c4124f;
  --hot:#e0195a;
  --violet:#4a1a8a;
  --white:#ffffff;
  --ink:#1c1c1c;
  --button:#4d0a35;
  --soft:#f2e9f2;
}
*{box-sizing:border-box;margin:0;padding:0}
html,body{width:1200px;height:4096px;overflow:hidden}
body{
  position:relative;
  font-family:"Roboto",Arial,sans-serif;color:var(--white);
  background:linear-gradient(180deg,#2a0a33 0px,#3b0b40 780px,#1e0a2c 1500px,#4b0f4b 1900px,#2c0b3f 2100px,#54114f 2450px,#6a1352 2700px,#3a0c3c 3100px,#5d0f46 3400px,#270b3c 3480px,#3c1052 3800px,#b0124c 4096px);
}
.abs{position:absolute}
h1,h2,h3,.heading{font-family:"Cabin",sans-serif;font-weight:600}

/* header */
.topbar{left:0;top:0;width:1200px;height:53px;background:#1b0a22;font-size:13px}
.topbar a{position:absolute;top:17px;color:var(--white);text-decoration:none}
.topbar .sep{position:absolute;top:0;width:1px;height:53px;background:rgba(255,255,255,.25)}
.icon-dot{position:absolute;top:12px;width:24px;height:24px;border-radius:50%;background:var(--white)}
.hero{left:0;top:53px;width:1200px;height:700px;
  background:linear-gradient(180deg,#e2154e 0%,#b41060 25%,#6d1880 55%,#3a1470 80%,#2a0a33 100%)}
.hero-scene{left:0;top:200px;width:1200px;height:550px;
  background:radial-gradient(ellipse 260px 240px at 600px 240px,rgba(255,120,80,.55),rgba(255,40,100,.2) 60%,transparent 70%),
  linear-gradient(180deg,transparent 0%,rgba(40,5,60,.35) 60%,rgba(30,8,40,.9) 100%)}
.nav a{position:absolute;top:82px;font-weight:700;font-size:15px;color:var(--white);text-decoration:none}
.logo-badge{left:520px;top:0;width:160px;height:180px}
.logo-name{left:520px;top:100px;width:160px;text-align:center;font-family:"Cabin",sans-serif;font-weight:500;font-size:22px}
.hero-title{left:0;top:345px;width:1200px;text-align:center;font-size:57px;line-height:72px;font-weight:600}
.btn-outline{display:flex;align-items:center;justify-content:center;gap:8px;
  border:2px solid var(--white);border-radius:6px;background:var(--magenta);
  font-weight:700;font-size:13px;text-transform:uppercase;color:var(--white)}
.chev{width:12px;height:12px;border-radius:50%;background:var(--white);position:relative}
.chev::after{content:"";position:absolute;left:3px;top:3px;width:4px;height:4px;border-right:2px solid var(--magenta);border-top:2px solid var(--magenta);transform:rotate(45deg)}

/* promos */
.promo{border-radius:4px;overflow:hidden}
.promo-photo{position:absolute;top:0;height:100%}
.promo-text{position:absolute;font-family:"Cabin",sans-serif}

/* sections */
.section-title{left:0;width:1200px;text-align:center;font-size:44px}
.product-card{width:232px;height:230px;background:var(--white);border-radius:4px;color:var(--ink);text-align:center}
.product-photo{position:absolute;left:50px;top:12px;width:132px;height:118px;border-radius:4px}
.product-name{position:absolute;left:0;top:138px;width:100%;font-size:13px}
.product-price{position:absolute;left:0;top:158px;width:100%;font-size:20px;font-weight:700}
.add-cart{position:absolute;left:12px;top:189px;width:208px;height:34px;background:var(--button);border-radius:4px;
  color:var(--white);font-size:13px;font-weight:700;line-height:34px}
.arrow{width:28px;height:28px;border-radius:50%;background:var(--white);margin:-14px 0 0 -14px}
.arrow::after{content:"";position:absolute;left:11px;top:10px;width:6px;height:6px;border-left:1.5px solid #333;border-bottom:1.5px solid #333;transform:rotate(45deg)}
.arrow.next::after{left:9px;transform:rotate(-135deg)}
.topic{height:282px;border-radius:2px}
.topic span{position:absolute;left:0;bottom:30px;width:100%;text-align:center;font-weight:700;font-size:17px}

/* blog */
.blog{left:121px;top:3016px;width:956px;height:369px;
  background:linear-gradient(100deg,#4a4a52 0%,#2c3142 35%,#1c2a4a 60%,#263040 100%)}
.blog-bar{left:146px;top:3294px;width:909px;height:75px;background:linear-gradient(90deg,#6b0c3e,#9c0f4a);border-radius:3px}

/* footer */
.newsletter{left:251px;top:3645px;width:696px;height:62px;background:var(--white);border-radius:4px}
.footer-col h4{font-size:14px;font-weight:700;margin-bottom:20px;letter-spacing:.3px}
.footer-col li{list-style:none;font-size:13px;line-height:25.5px}
.social{width:18px;height:18px;border-radius:50%;background:var(--white);top:4016px}
</style>
</head>
<body>

<!-- Hero -->
<div class="abs hero"></div>
<div class="abs hero-scene" role="img" aria-label="Retro sunset beach scene with palm trees and a couple silhouette"></div>
<div class="abs topbar">
  <a style="left:113px">Find a Retailer</a>
  <span class="sep" style="left:230px"></span>
  <a style="left:260px">Need Help?</a>
  <span class="sep" style="left:350px"></span>
  <span class="icon-dot" style="left:901px"></span>
  <span class="icon-dot" style="left:935px"></span>
  <span class="icon-dot" style="left:969px"></span>
  <a style="left:1031px">&#9679; Log In</a>
</div>
<nav class="nav">
  <a style="left:113px">Home</a>
  <a style="left:217px">About</a>
  <a style="left:320px">Products</a>
  <a style="left:814px">Tutorials</a>
  <a style="left:936px">Contact</a>
  <a style="left:1051px">Shop</a>
</nav>
<svg class="abs logo-badge" viewBox="0 0 160 180"><path d="M0 0H160V140L80 180L0 140Z" fill="#1d0a22"/><rect x="60" y="30" width="40" height="40" fill="#fff"/></svg>
<div class="abs logo-name">Kitlorne</div>
<h1 class="abs hero-title">Experience the Future with<br>Our Electronic Kits!</h1>
<div class="abs btn-outline" style="left:515px;top:539px;width:170px;height:48px">View Products <span class="chev"></span></div>

<!-- Promos -->
<div class="abs promo" style="left:25px;top:815px;width:633px;height:315px;background:linear-gradient(90deg,#8a8a90 0%,#5a3a60 40%,#3a0c3a 70%,#2a0a2e 100%)" role="img" aria-label="Hands repairing a laptop motherboard"></div>
<div class="abs promo-text" style="left:365px;top:855px;font-size:26px;line-height:40px">Lorem ipsum dolor sit<br>amet, consectetur</div>
<div class="abs promo-text" style="left:408px;top:950px;font-size:26px">Get Offer <span style="font-size:54px;font-weight:700;vertical-align:-6px">30%</span></div>
<div class="abs btn-outline" style="left:441px;top:1032px;width:170px;height:46px">View Products <span class="chev"></span></div>

<div class="abs promo" style="left:683px;top:815px;width:490px;height:315px;background:linear-gradient(90deg,#e8eaee 0%,#a9a5b5 40%,#3a0c3a 70%,#220a2a 100%)" role="img" aria-label="Assorted circuit boards and electronic components"></div>
<div class="abs promo-text" style="left:967px;top:898px;font-size:26px">Electonic Parts</div>
<div class="abs" style="left:968px;top:956px;font-size:15px;line-height:28px">Lorem ipsum dolor sit<br>amet, consectetur</div>
<div class="abs btn-outline" style="left:967px;top:1049px;width:170px;height:46px">View Products <span class="chev"></span></div>

<div class="abs promo" style="left:25px;top:1167px;width:490px;height:313px;background:linear-gradient(270deg,#a69aa0 0%,#6a3a58 45%,#3a0c3a 70%,#2a0a2e 100%)" role="img" aria-label="Father and daughter building an electronics kit"></div>
<div class="abs heading" style="left:66px;top:1191px;width:138px;height:42px;background:#fff;border-radius:4px;color:#1c1c1c;font-size:32px;line-height:42px;text-align:center">500+</div>
<div class="abs promo-text" style="left:64px;top:1250px;font-size:34px">Electronic kits</div>
<div class="abs" style="left:73px;top:1313px;font-size:15px;line-height:28px;font-weight:700">Lorem ipsum dolor sit amet,<br>consectetur</div>

<div class="abs promo" style="left:542px;top:1167px;width:631px;height:313px;background:linear-gradient(90deg,#240a2c 0%,#3a0c3a 35%,#8a7380 65%,#d8d6d8 100%)" role="img" aria-label="Young man recording a tutorial with a microphone"></div>
<div class="abs promo-text" style="left:577px;top:1218px;font-size:34px;line-height:50px">Tutorials for<br>Hobbyists</div>
<div class="abs btn-outline" style="left:582px;top:1345px;width:170px;height:46px">View More <span class="chev"></span></div>

<!-- Our Products -->
<h2 class="abs section-title" style="top:1588px">Our Products</h2>
<div class="abs arrow" style="left:75px;top:1797px"></div>
<div class="abs arrow next" style="left:1124px;top:1797px"></div>
<div class="abs product-card" style="left:111px;top:1691px"><div class="product-photo" style="background:radial-gradient(#3a3a3a,#eee 75%)" role="img" aria-label="Battery cells"></div><div class="product-name">Flexline 2.0 Wireless Shield</div><div class="product-price">$260.00</div><div class="add-cart">ADD TO CART</div></div>
<div class="abs product-card" style="left:359px;top:1691px"><div class="product-photo" style="background:radial-gradient(#9a9a9a,#f2f2f2 70%)" role="img" aria-label="Spark plug component"></div><div class="product-name">Flexline 2.0 Wireless Shield</div><div class="product-price">$260.00</div><div class="add-cart">ADD TO CART</div></div>
<div class="abs product-card" style="left:609px;top:1691px"><div class="product-photo" style="background:radial-gradient(#d9c96a,#f6f6f6 60%)" role="img" aria-label="Small capacitor with leads"></div><div class="product-name">Flexline 2.0 Wireless Shield</div><div class="product-price">$260.00</div><div class="add-cart">ADD TO CART</div></div>
<div class="abs product-card" style="left:857px;top:1691px"><div class="product-photo" style="background:radial-gradient(#2f6aa8,#e9eef4 75%)" role="img" aria-label="Blue microcontroller board"></div><div class="product-name">Flexline 2.0 Wireless Shield</div><div class="product-price">$260.00</div><div class="add-cart">ADD TO CART</div></div>

<!-- Topics -->
<h2 class="abs section-title" style="top:2017px">Learn About Popular Electronics Topics</h2>
<div class="abs arrow" style="left:75px;top:2252px"></div>
<div class="abs arrow next" style="left:1124px;top:2252px"></div>
<div class="abs topic" style="left:113px;top:2133px;width:295px;background:linear-gradient(180deg,#8a9098,#4a4e58 60%,#2a2a33)" role="img" aria-label="Engineer in a hard hat working on wiring"><span>Engineering Essentials</span></div>
<div class="abs topic" style="left:450px;top:2133px;width:294px;background:radial-gradient(ellipse at 55% 45%,#3a8cff,#1a2a80 40%,#0a0a1a 75%)" role="img" aria-label="Glowing wireless signal graphic"><span>Working with WiFi</span></div>
<div class="abs topic" style="left:785px;top:2133px;width:296px;background:linear-gradient(180deg,#4a4048,#a0352a 55%,#3a2a2e)" role="img" aria-label="Cyclist in a red jacket with a helmet"><span>Building a GPS System</span></div>

<!-- Featured -->
<h2 class="abs section-title" style="top:2505px">Featured Products</h2>
<div class="abs arrow" style="left:75px;top:2714px"></div>
<div class="abs arrow next" style="left:1124px;top:2714px"></div>
<div class="abs product-card" style="left:111px;top:2608px"><div class="product-photo" style="background:radial-gradient(#d6b020,#f4f4f4 70%)" role="img" aria-label="Screwdriver bit set"></div><div class="product-name">Flexline 2.0 Wireless Shield</div><div class="product-price">$260.00</div><div class="add-cart">ADD TO CART</div></div>
<div class="abs product-card" style="left:359px;top:2608px"><div class="product-photo" style="background:radial-gradient(#6a6a6a,#f4f4f4 65%)" role="img" aria-label="Analog multimeter with test leads"></div><div class="product-name">Flexline 2.0 Wireless Shield</div><div class="product-price">$260.00</div><div class="add-cart">ADD TO CART</div></div>
<div class="abs product-card" style="left:609px;top:2608px"><div class="product-photo" style="background:radial-gradient(#4a7ad0,#f4f4f4 70%)" role="img" aria-label="Colourful wired circuit module"></div><div class="product-name">Flexline 2.0 Wireless Shield</div><div class="product-price">$260.00</div><div class="add-cart">ADD TO CART</div></div>
<div class="abs product-card" style="left:857px;top:2608px"><div class="product-photo" style="background:radial-gradient(#b07a3a,#f4f4f4 65%)" role="img" aria-label="Copper coil and connector parts"></div><div class="product-name">Flexline 2.0 Wireless Shield</div><div class="product-price">$260.00</div><div class="add-cart">ADD TO CART</div></div>

<!-- Blogs -->
<h2 class="abs section-title" style="top:2928px">Our Blogs</h2>
<div class="abs arrow" style="left:75px;top:3210px"></div>
<div class="abs arrow next" style="left:1124px;top:3210px"></div>
<div class="abs blog" role="img" aria-label="Two technicians discussing server room cabling"></div>
<div class="abs blog-bar"></div>
<div class="abs heading" style="left:169px;top:3316px;font-size:24px;font-weight:700">What Are You Working On?</div>
<div class="abs" style="left:481px;top:3308px;width:1px;height:48px;background:rgba(255,255,255,.6)"></div>
<div class="abs" style="left:507px;top:3310px;font-size:13px;line-height:25px">We want to see what types of projects you all<br>are using your Quimzaloft parts for!</div>
<div class="abs btn-outline" style="left:871px;top:3308px;width:170px;height:48px">View More <span class="chev"></span></div>

<!-- Newsletter -->
<h2 class="abs" style="left:0;top:3563px;width:1200px;text-align:center;font-family:'Cabin',sans-serif;font-weight:500;font-size:32px">STAY IN TOUCH WITH US</h2>
<div class="abs newsletter">
  <span class="abs" style="left:24px;top:23px;font-size:13px;color:#777">ENTER EMAIL ADDRESS</span>
  <span class="abs" style="left:518px;top:9px;width:166px;height:44px;background:var(--magenta);border-radius:4px;text-align:center;line-height:44px;font-weight:700;font-size:14px">SUBMIT</span>
</div>

<!-- Footer -->
<div class="abs footer-col" style="left:113px;top:3800px"><h4>ABOUT</h4><ul><li>Read Our Story</li><li>Press &amp; Media</li><li>Success with Kitlorne</li><li>KitlorneFun Education</li><li>Job Openings</li></ul></div>
<div class="abs footer-col" style="left:362px;top:3800px"><h4>PARTNER WITH US</h4><ul><li>See Our Partners</li><li>Become a Distributor/Reseller</li><li>Receive Volume Discounts</li><li>Explore Custom Kits</li><li>Apply for a Hardware Donation</li></ul></div>
<div class="abs footer-col" style="left:644px;top:3800px"><h4>SUPPORT</h4><ul><li>Customer Support</li><li>Purchase Orders &amp; Payment Terms</li><li>Technical Assistance</li><li>FAQs</li><li>Contact Us</li></ul></div>
<div class="abs footer-col" style="left:930px;top:3800px"><h4>INFORMATION</h4><ul><li>Terms of Service</li><li>Privacy Policy</li><li>Accessibility Statement</li><li>Compliance</li><li>Site Map</li></ul></div>
<span class="abs social" style="left:546px"></span>
<span class="abs social" style="left:576px"></span>
<span class="abs social" style="left:606px"></span>
<span class="abs social" style="left:636px"></span>
<div class="abs" style="left:0;top:4066px;width:1200px;text-align:center;font-size:10px">COPYRIGHT@2024 - ALL RIGHTS RESERVED BY KITLORNE</div>

</body>
</html>
```